Business Card for Fashion House

We need a business card design for our personalize fashion service for our customers. the business card should reflect reliability, luxury and creativity.
The brand Gravetto is extracted from "Graceful Vetto"; Gravetto provides fashion designs sprinkled with luxury and style tailored for our elite clients character profile.
Gravetto is created for those who embody class and elegance with a passion for style.
Target Market(s)
Affluent Customers
Industry/Entity Type
Fashion
Contact Information for Business Card
Rania Bou Khalil
Fashion Designer
Telephone: +971 5550123
Mobile +971 555987
Emal q@z.com
Website www.gravetto-example.com
Social Media Youtube g+ Facebook Instagram Pin /gravetto
Font styles to use
Other font styles liked:
- Audrey provided
Look and feel
Each slider illustrates characteristics of the customer's brand and the style your logo design should communicate.

```html
<!DOCTYPE html>
<html lang="en">
<head>
<meta charset="UTF-8">
<title>Gravetto Business Card</title>
<link href="https://fonts.googleapis.com/css2?family=Cinzel:wght@400&family=Great+Vibes&family=Montserrat:wght@300;400&display=swap" rel="stylesheet">
<style>
  :root {
    --backdrop: #2a2a2b;
    --card: #141415;
    --card-edge: #1d1d1f;
    --silver: #d4d6d9;
    --silver-dim: #9a9da2;
    --text-light: #e6e6e6;
  }
  * { margin: 0; padding: 0; box-sizing: border-box; }
  html, body {
    width: 800px; height: 1200px; overflow: hidden;
    background: var(--backdrop);
    font-family: "Montserrat", sans-serif;
  }
  .canvas {
    position: relative; width: 800px; height: 1200px;
    display: flex; flex-direction: column; align-items: center; justify-content: center; gap: 120px;
  }
  .card {
    position: relative; width: 620px; height: 360px;
    background: linear-gradient(145deg, var(--card-edge), var(--card));
    box-shadow: 0 18px 40px rgba(0,0,0,.55);
    overflow: hidden;
  }
  /* Front */
  .card-front { display: flex; flex-direction: column; align-items: center; justify-content: center; gap: 26px; }
  .front-mark {
    width: 54px; height: 54px; border-radius: 50%;
    border: 3px solid var(--silver-dim);
  }
  .front-name {
    font-family: "Cinzel", serif; font-size: 34px; letter-spacing: 16px;
    color: var(--silver); padding-left: 16px;
  }
  /* Back */
  .back-brand {
    position: absolute; left: 44px; top: 34px;
    font-family: "Cinzel", serif; font-size: 20px; letter-spacing: 9px; color: var(--silver);
  }
  .person { position: absolute; left: 44px; top: 112px; }
  .person-name { font-family: "Great Vibes", cursive; font-size: 30px; color: var(--text-light); line-height: 1; }
  .person-role { font-size: 9px; letter-spacing: 1px; color: var(--silver-dim); margin-top: 4px; }
  .contacts { position: absolute; left: 44px; top: 182px; list-style: none; }
  .contacts li {
    display: flex; align-items: center; gap: 9px;
    font-size: 10.5px; color: var(--text-light); height: 20px; letter-spacing: .3px;
  }
  .contacts svg { width: 11px; height: 11px; flex: none; }
  .social-dot { width: 10px; height: 10px; border-radius: 50%; background: var(--silver-dim); flex: none; }
  .back-emblem {
    position: absolute; right: -40px; top: 60px; width: 300px; height: 300px;
    border-radius: 50%; border: 10px solid var(--silver);
    display: flex; align-items: center; justify-content: center;
  }
  .back-emblem span {
    font-family: "Cinzel", serif; font-size: 22px; letter-spacing: 6px; color: var(--silver);
    margin-right: 30px;
  }
</style>
</head>
<body>
<main class="canvas">
  <section class="card card-front">
    <div class="front-mark"></div>
    <div class="front-name">GRAVETTO</div>
  </section>

  <section class="card card-back">
    <div class="back-brand">GRAVETTO</div>
    <div class="person">
      <div class="person-name">Rania Bou Khalil</div>
      <div class="person-role">Fashion Designer</div>
    </div>
    <ul class="contacts">
      <li>
        <svg viewBox="0 0 24 24" fill="none" stroke="#d4d6d9" stroke-width="2"><path d="M5 3h4l2 5-3 2a12 12 0 0 0 6 6l2-3 5 2v4a2 2 0 0 1-2 2A18 18 0 0 1 3 5a2 2 0 0 1 2-2z"/></svg>
        +971 5550123
      </li>
      <li>
        <svg viewBox="0 0 24 24" fill="none" stroke="#d4d6d9" stroke-width="2"><rect x="6" y="2" width="12" height="20" rx="2"/><line x1="11" y1="18" x2="13" y2="18"/></svg>
        +971 555987
      </li>
      <li>
        <svg viewBox="0 0 24 24" fill="none" stroke="#d4d6d9" stroke-width="2"><rect x="2" y="5" width="20" height="14" rx="1"/><path d="M2 6l10 7 10-7"/></svg>
        q@z.com
      </li>
      <li>
        <svg viewBox="0 0 24 24" fill="none" stroke="#d4d6d9" stroke-width="2"><circle cx="12" cy="12" r="10"/><path d="M2 12h20M12 2c3 3 3 17 0 20M12 2c-3 3-3 17 0 20"/></svg>
        www.gravetto-example.com
      </li>
      <li>
        <span class="social-dot"></span>
        /gravetto
      </li>
    </ul>
    <div class="back-emblem"><span>GRAVETTO</span></div>
  </section>
</main>
</body>
</html>
```